Utility Contractor looking for a new website

Water and wastewater utility contractor looking to create a new website that highlights our various services. We are looking for modern web presence that can be updated with current projects and new services as we grow. We have an existing logo that we would like to incorporate into the overall design of the site
Updates

Hi, Thank you for all the design submissions. I have had some time to review and have eliminated the ones I feel are not what I am looking for. Based on the designs that remain, I am looking for a clean (not to many bold colours), modern look that is not to busy (long scrolling page), Thanks, Dean

Target Market(s)

project managers, strata boards, owners, people who make decisions as to who operates their water/wastewater system

Industry/Entity Type

Utility

Font styles to use
Sans Serif

Requirements
Must have
• A min page that describes the company and what we do, A page for each of our services that outlines the service and the benefits of it. the look must be consistent throughout. additionally each service page should have some images related to the service

```html
<!DOCTYPE html>
<html lang="en">
<head>
<meta charset="utf-8">
<title>Clearline Waterworks Ltd.</title>
<link href="https://fonts.googleapis.com/css2?family=Mulish:wght@400;600;700;800&display=swap" rel="stylesheet">
<style>
:root{
  --blue:#2a7fc1;
  --blue-dark:#1f6aa6;
  --navy:#14365e;
  --ink:#1e2a3a;
  --grey-text:#8a8a8a;
  --grey-line:#e6e6e6;
  --sky:#5fc7ee;
  --white:#ffffff;
  --field:#a9d3f0;
}
*{box-sizing:border-box;margin:0;padding:0}
html,body{width:960px;height:1200px;overflow:hidden;background:var(--white)}
body{font-family:"Mulish",sans-serif;color:var(--ink);position:relative}
.abs{position:absolute}

/* header */
.top-rule{left:0;top:0;width:960px;height:2px;background:var(--blue)}
.site-header{left:0;top:2px;width:960px;height:68px;background:var(--white);box-shadow:0 2px 4px rgba(0,0,0,.12);z-index:2}
.brand{left:104px;top:20px;display:flex;align-items:center;gap:8px}
.brand-dot{width:12px;height:12px;border-radius:50%;background:var(--navy)}
.brand-name{font-weight:800;font-size:15px;line-height:15px;color:var(--navy);letter-spacing:-.2px}
.main-nav{left:398px;top:24px;display:flex;align-items:center;font-size:11.5px;color:var(--ink)}
.main-nav a{color:inherit;text-decoration:none;margin-right:24px}
.main-nav a.active{background:var(--blue);color:var(--white);padding:6px 13px;margin-right:22px}

/* hero */
.hero{left:0;top:70px;width:960px;height:386px;background:linear-gradient(100deg,#9aa2ad 0%,#c9cdd3 35%,#d9dde2 55%,#a7adb5 75%,#c7cbd0 100%)}
.hero-headline{left:104px;top:224px;font-size:23px;line-height:41.5px;color:var(--white);font-weight:400;text-transform:uppercase;letter-spacing:-.3px}
.hero-headline b{font-weight:800}
.hero-headline .accent{color:var(--sky);font-weight:800}
.hero-arrow{top:244px}

/* welcome */
.welcome-title{left:0;top:488px;width:960px;text-align:center;font-size:21px;color:var(--navy)}
.welcome-title span{color:var(--blue);margin-right:8px}
.welcome-text{left:135px;top:528px;width:690px;text-align:center;font-size:11px;line-height:17.3px;color:var(--grey-text)}

.feature{top:606px;width:240px;height:92px;border:5px solid var(--grey-line);background:var(--white);padding:20px 0 0 70px}
.feature-icon{position:absolute;left:10px;top:13px}
.feature h3{font-size:11px;font-weight:700;color:var(--navy);margin-bottom:4px;margin-left:-4px}
.feature p{font-size:8.6px;line-height:12.8px;color:var(--grey-text)}

/* latest works */
.works-title{left:104px;top:740px;font-size:15px;color:var(--blue)}
.works-text{left:104px;top:771px;width:180px;font-size:9px;line-height:15.8px;color:var(--grey-text)}
.works-text p{margin-bottom:15px}
.btn-more{left:105px;top:1000px;width:78px;height:22px;background:var(--blue);color:var(--white);font-size:8.5px;font-weight:700;display:flex;align-items:center;justify-content:center}
.works-pager{left:253px;top:1005px}
.work-tile{width:173px;height:130px}

/* footer */
.site-footer{left:0;top:1058px;width:960px;height:142px;background:var(--blue)}
.subscribe{left:106px;top:1083px;width:450px;height:51px;background:#5ba6dc;border-radius:2px}
.subscribe-field{left:113px;top:1090px;width:305px;height:38px;background:var(--field);color:var(--white);font-size:9.5px;display:flex;align-items:center;padding-left:13px}
.subscribe-btn{left:426px;top:1090px;width:122px;height:38px;background:var(--field);color:var(--white);font-size:13px;display:flex;align-items:center;justify-content:center}
.follow{left:613px;top:1093px;font-size:19px;color:var(--white)}
.social{top:1090px;width:30px;height:30px;border-radius:50%;background:var(--white)}
.footer-nav{left:106px;top:1158px;font-size:11px;color:var(--white)}
.footer-nav span{margin:0 4px}
.copyright{left:687px;top:1148px;font-size:9.5px;color:var(--white)}
</style>
</head>
<body>
  <div class="abs top-rule"></div>
  <header class="abs site-header">
    <div class="abs brand" style="top:18px">
      <div class="brand-dot"></div>
      <div class="brand-name">CLEARLINE<br>WATERWORKS LTD.</div>
    </div>
    <nav class="abs main-nav">
      <a class="active">HOME</a>
      <a>ABOUT</a>
      <a>SERVICE</a>
      <a>PROJECTS</a>
      <a>GALLERY</a>
      <a>NEWS</a>
      <a style="margin-right:0">CONTACTS</a>
    </nav>
  </header>

  <section class="abs hero" role="img" aria-label="Photo of a polished chrome bathroom faucet on a tiled sink"></section>
  <h1 class="abs hero-headline">
    Amet conse <b>ctetur adipisicing elit,</b><br>
    Sed do eiusmod tempor <b>inciostrud</b><br>
    <span class="accent">Exercitation</span> ullamco.
  </h1>
  <svg class="abs hero-arrow" style="left:9px" width="38" height="38" viewBox="0 0 38 38">
    <circle cx="19" cy="19" r="17" fill="none" stroke="#fff" stroke-width="2"/>
    <path d="M23 10 L12 19 L23 28 Z" fill="#fff"/>
  </svg>
  <svg class="abs hero-arrow" style="left:910px" width="38" height="38" viewBox="0 0 38 38">
    <circle cx="19" cy="19" r="17" fill="none" stroke="#fff" stroke-width="2"/>
    <path d="M15 10 L26 19 L15 28 Z" fill="#fff"/>
  </svg>

  <h2 class="abs welcome-title"><span>WELCOME TO</span>CLEARLINE WATERWORKS</h2>
  <p class="abs welcome-text">Sed ut perspiciatis unde omnis iste natus error sit voluptatem accusantium doloremque laudantium, totam rem aperiam, eaque ipsa quae ab illo inventore veritatis et quasi architecto beatae vitae dicta sunt explicabo. Nemo enim ipsam voluptatem quia voluptas sit aspernatur aut o dit aut fugit, sed quia consequuntur magni dolores eos qui ratione voluptatem sequi nesciunt. Neque porro</p>

  <article class="abs feature" style="left:105px">
    <svg class="feature-icon" width="56" height="56" viewBox="0 0 56 56">
      <circle cx="28" cy="28" r="25" fill="#fff" stroke="#ececec" stroke-width="5"/>
      <path d="M18 38 L36 20 M18 20 L36 38" stroke="#1f6aa6" stroke-width="3.5" stroke-linecap="round"/>
      <circle cx="37" cy="19" r="4" fill="none" stroke="#1f6aa6" stroke-width="2.5"/>
    </svg>
    <h3>Vivamus vel eros eget ma</h3>
    <p>Cnsectetuer adipiscing elit, sed diam nonummy nibh euismod tincidunt ut laoreet dolore magn.</p>
  </article>
  <article class="abs feature" style="left:360px">
    <svg class="feature-icon" width="56" height="56" viewBox="0 0 56 56">
      <circle cx="28" cy="28" r="25" fill="#fff" stroke="#ececec" stroke-width="5"/>
      <circle cx="28" cy="28" r="10" fill="none" stroke="#1f6aa6" stroke-width="4"/>
      <path d="M21 21 L24 24 M35 21 L32 24 M21 35 L24 32 M35 35 L32 32" stroke="#1f6aa6" stroke-width="3"/>
    </svg>
    <h3>Vivamus vel eros eget ma</h3>
    <p>Cnsectetuer adipiscing elit, sed diam nonummy nibh euismod tincidunt ut laoreet dolore magn.</p>
  </article>
  <article class="abs feature" style="left:615px">
    <svg class="feature-icon" width="56" height="56" viewBox="0 0 56 56">
      <circle cx="28" cy="28" r="25" fill="#fff" stroke="#ececec" stroke-width="5"/>
      <circle cx="28" cy="28" r="12" fill="#1f6aa6"/>
      <text x="28" y="33" text-anchor="middle" font-family="Mulish,sans-serif" font-weight="800" font-size="14" fill="#fff">?</text>
    </svg>
    <h3>Vivamus vel eros eget ma</h3>
    <p>Cnsectetuer adipiscing elit, sed diam nonummy nibh euismod tincidunt ut laoreet dolore magn.</p>
  </article>

  <h2 class="abs works-title">LATEST WORKS</h2>
  <div class="abs works-text">
    <p>Sed ut perspiciatis unde omnis iste natus error sit voluptatem accusantium dolo remque laudantium, totam rem aperiam, eaque ipsa quae.</p>
    <p>A illo inventore veritatis et quasi archite cto beatae vitae dicta sunt explicabo. Ne mo enim ipsam voluptatem quia volup tas sit aspernatur aut.</p>
    <p>Ait aut fugit, sed quia consequuntur mag ni dolores eos qui ratione voluptatem se qui nesciunt. Neque porro</p>
  </div>
  <div class="abs btn-more">MORE WORKS</div>
  <svg class="abs works-pager" width="22" height="12" viewBox="0 0 22 12">
    <path d="M8 1 L3 6 L8 11 M14 1 L19 6 L14 11" fill="none" stroke="#555" stroke-width="2"/>
  </svg>

  <div class="abs work-tile" style="left:300px;top:743px;background:linear-gradient(135deg,#e8ecef,#b9c0c7 60%,#3d4450)" role="img" aria-label="Plumber repairing pipes under a bathtub"></div>
  <div class="abs work-tile" style="left:492px;top:743px;background:linear-gradient(135deg,#e0a24a,#c4703a 55%,#7a3a22)" role="img" aria-label="Indoor decorative water fountain in a warm lounge"></div>
  <div class="abs work-tile" style="left:682px;top:743px;background:linear-gradient(135deg,#e9f3fb,#a9d2ef 55%,#3a8fd0)" role="img" aria-label="Blue mosaic swimming pool tiles"></div>
  <div class="abs work-tile" style="left:300px;top:892px;background:linear-gradient(160deg,#d8e0e2,#7fb6c6 55%,#1f6f8a)" role="img" aria-label="Indoor swimming pool with steel ladder"></div>
  <div class="abs work-tile" style="left:492px;top:892px;background:linear-gradient(160deg,#e4e6e2,#a7aaa2 55%,#5b5e58)" role="img" aria-label="Flooded modern living room interior"></div>
  <div class="abs work-tile" style="left:682px;top:892px;background:linear-gradient(135deg,#2a2c30,#6d7178 50%,#d9dadb)" role="img" aria-label="Technician fitting drain pipework under a sink"></div>

  <footer class="abs site-footer"></footer>
  <div class="abs subscribe"></div>
  <div class="abs subscribe-field">Please enter your Email address</div>
  <div class="abs subscribe-btn">SUBSCRIBE HERE</div>
  <div class="abs follow">Follow Us</div>
  <div class="abs social" style="left:706px"></div>
  <div class="abs social" style="left:746px"></div>
  <div class="abs social" style="left:786px"></div>
  <div class="abs social" style="left:826px"></div>
  <nav class="abs footer-nav">HOME<span>|</span>ABOUT<span>|</span>SERVICE<span>|</span>PROJECTS<span>|</span>GALLERY<span>|</span>NEWS<span>|</span>CONTACTS</nav>
  <div class="abs copyright">Copyright © 2014 all rights are reseved</div>
</body>
</html>
```